Super elegant, crisp & clean Business card design required

We recently upgraded our branding - which is on our website - tavorelstudio.com

I would like a simple, yet elegant, clean business card design please.

The font of my logo is Cinzel - and because of the natural colour - it's best to have this on a black background.

I would like to have the back of the business card - with simply my logo.

PLEASE DO NOT SUBMIT A COMPLICATED / UNCLEAN DESIGN

Industry/Entity Type

Business

Contact Information for Business Card

Dalvik Ostrander Photography

Font styles to use
Other font styles liked:
• Cinzel

Requirements
Must have
• A backpage with nothing but my logo
• Simple design - stands out
Should not have
• Colour that dont align with my logo
• Over complicated '/ non symmetrical design

```html
<!DOCTYPE html>
<html lang="en">
<head>
<meta charset="utf-8">
<title>Dalvik Ostrander Photography — Business Card</title>
<link rel="stylesheet" href="https://fonts.googleapis.com/css2?family=Cinzel:wght@400;600&family=Open+Sans:wght@400;600&display=swap">
<style>
  :root {
    --backdrop: #eef0ee;
    --card-white: #fbfbf9;
    --card-black: #0b0b0b;
    --gold: #a88d5e;
    --gold-soft: #b49a6c;
    --shadow: rgba(0, 0, 0, 0.14);
  }
  * { margin: 0; padding: 0; box-sizing: border-box; }
  html, body {
    width: 1200px;
    height: 1006px;
    overflow: hidden;
    background: var(--backdrop);
  }
  .canvas {
    width: 1200px;
    height: 1006px;
    display: flex;
    align-items: center;
    justify-content: center;
    gap: 90px;
  }
  .card {
    width: 380px;
    height: 650px;
    box-shadow: 0 12px 30px var(--shadow);
    display: flex;
    flex-direction: column;
    align-items: center;
    color: var(--gold);
    text-align: center;
  }
  .card--front { background: var(--card-white); padding-top: 120px; }
  .card--back { background: var(--card-black); justify-content: center; }

  .brand { display: flex; flex-direction: column; align-items: center; }
  .brand__square {
    border: 1.5px solid var(--gold);
  }
  .card--front .brand__square { width: 62px; height: 62px; margin-bottom: 14px; }
  .card--back .brand__square { width: 180px; height: 200px; margin-bottom: 26px; border-color: var(--gold-soft); }

  .brand__name {
    font-family: "Cinzel", serif;
    font-weight: 400;
    color: var(--gold);
    line-height: 1.35;
    letter-spacing: 0.06em;
  }
  .card--front .brand__name { font-size: 15px; }
  .card--back .brand__name { font-size: 25px; color: var(--gold-soft); }
  .brand__name span { display: block; letter-spacing: 0.42em; }
  .card--front .brand__name span { font-size: 10px; }
  .card--back .brand__name span { font-size: 15px; }

  .contact {
    margin-top: 92px;
    font-family: "Open Sans", sans-serif;
  }
  .contact__name {
    font-size: 21px;
    font-weight: 600;
    letter-spacing: 0.04em;
    text-transform: uppercase;
  }
  .contact__role { font-size: 14px; margin-top: 2px; color: var(--gold-soft); }
  .contact__lines { margin-top: 26px; font-size: 15px; line-height: 1.6; }
  .contact__web { font-size: 12px; letter-spacing: 0.03em; text-transform: uppercase; }
</style>
</head>
<body>
  <main class="canvas">
    <section class="card card--front" aria-label="Business card front">
      <div class="brand">
        <div class="brand__square"></div>
        <p class="brand__name">Dalvik Ostrander<span>Photography</span></p>
      </div>
      <div class="contact">
        <p class="contact__name">Elias Marrow</p>
        <p class="contact__role">Photographer</p>
        <div class="contact__lines">
          <p>123 456 789</p>
          <p>lorem@ipsum.com</p>
          <p class="contact__web">tavorelstudio.com</p>
        </div>
      </div>
    </section>

    <section class="card card--back" aria-label="Business card back">
      <div class="brand">
        <div class="brand__square"></div>
        <p class="brand__name">Dalvik Ostrander<span>Photography</span></p>
      </div>
    </section>
  </main>
</body>
</html>
```